Velvet Orchid Beauty Bar Business Card

We need a modern, elegant business card design for our new beauty bar located in La Quinta, CA. The card should feel premium yet approachable, reflecting our brand identity: warm, stylish, and confidence-boosting.

Use our existing Velvet Orchid Beauty Bar logo (to be provided as vector file).

Colors: Black, White, Blush / Nude accents, and Gold (metallic or foil effect if possible).

Typography: Clean sans-serif for clarity, with optional elegant script accent.
Design Style

Minimalist and modern with plenty of white space.

Premium look with a beauty/lifestyle feel (not overly corporate).

Option to explore vertical or horizontal orientation.

Rounded corners welcome, but not required.

Additional Notes

Design should print well in both matte and glossy finishes.

Please present mockups with both light and dark backgrounds.

Keep overall feel sleek, feminine, and high-end while still being approachable.

```html
<!DOCTYPE html>
<html lang="en">
<head>
<meta charset="utf-8">
<title>Velvet Orchid Beauty Bar – Business Card</title>
<link rel="stylesheet" href="https://fonts.googleapis.com/css2?family=Open+Sans:wght@400;600&family=Arvo:wght@700&display=swap">
<style>
  :root {
    --backdrop: #2b2b2d;
    --card: #1e1e1f;
    --card-edge: #b58f2c;
    --gold: #d2a534;
    --emboss-dark: #111112;
    --emboss-light: #2c2c2e;
  }
  * { box-sizing: border-box; margin: 0; padding: 0; }
  html, body { width: 1200px; height: 801px; overflow: hidden; }
  body {
    background: var(--backdrop);
    font-family: "Open Sans", Arial, sans-serif;
    display: flex;
    align-items: center;
    justify-content: center;
    gap: 40px;
  }
  .card {
    position: relative;
    width: 540px;
    height: 309px;
    background: var(--card);
    border: 2px solid var(--card-edge);
    border-radius: 14px;
    box-shadow: 0 18px 40px rgba(0,0,0,.45);
  }
  .brand {
    position: absolute;
    left: 0; right: 0;
    text-align: center;
  }
  .brand__tagline {
    font-size: 13px;
    letter-spacing: .5px;
    margin-bottom: 4px;
  }
  .brand__name {
    font-weight: 600;
    font-size: 30px;
    line-height: 1.1;
    letter-spacing: 1px;
  }
  .brand__sub {
    font-size: 15px;
    margin-top: 4px;
    display: flex;
    align-items: center;
    justify-content: center;
    gap: 8px;
  }
  .brand__sub::before,
  .brand__sub::after {
    content: "";
    width: 22px;
    height: 1px;
    background: currentColor;
  }
  /* back side: blind emboss */
  .card--back .brand { top: 104px; color: var(--emboss-dark); text-shadow: 0 1px 0 var(--emboss-light); }
  .card--back .brand__sub::before,
  .card--back .brand__sub::after { box-shadow: 0 1px 0 var(--emboss-light); }
  /* front side: gold foil */
  .card--front { color: var(--gold); }
  .card--front .brand { top: 40px; }
  .holder {
    position: absolute;
    left: 50px;
    top: 180px;
    width: 200px;
    text-align: right;
  }
  .holder__name { font-family: "Arvo", Georgia, serif; font-weight: 700; font-size: 22px; }
  .holder__role { font-size: 13px; margin-top: 2px; }
  .divider {
    position: absolute;
    left: 268px;
    top: 168px;
    width: 1.5px;
    height: 72px;
    background: var(--gold);
  }
  .contact {
    position: absolute;
    left: 284px;
    top: 170px;
    list-style: none;
    font-size: 12.5px;
  }
  .contact li { display: flex; align-items: center; gap: 8px; height: 23px; white-space: nowrap; }
  .contact svg { width: 13px; height: 13px; fill: none; stroke: var(--gold); stroke-width: 1.6; flex: none; }
  .address {
    position: absolute;
    left: 0; right: 0;
    bottom: 28px;
    text-align: center;
    font-size: 13px;
    letter-spacing: .3px;
  }
</style>
</head>
<body>
  <section class="card card--back" aria-label="Card back">
    <div class="brand">
      <p class="brand__tagline">Your Beauty, Your Style.</p>
      <p class="brand__name">VELVET ORCHID</p>
      <p class="brand__sub">Beauty Bar by Marisol</p>
    </div>
  </section>

  <section class="card card--front" aria-label="Card front">
    <div class="brand">
      <p class="brand__tagline">Your Beauty, Your Style.</p>
      <p class="brand__name">VELVET ORCHID</p>
      <p class="brand__sub">Beauty Bar by Marisol</p>
    </div>

    <div class="holder">
      <p class="holder__name">Marisol Reyes</p>
      <p class="holder__role">Owner</p>
    </div>

    <div class="divider"></div>

    <ul class="contact">
      <li>
        <svg viewBox="0 0 16 16" aria-hidden="true"><path d="M4 2l2.5 3-1.5 1.5c1 2 2.5 3.5 4.5 4.5L11 9.5l3 2.5-1.5 2C7 14 2 9 2 3.5z"/></svg>
        760-555-0142
      </li>
      <li>
        <svg viewBox="0 0 16 16" aria-hidden="true"><rect x="1.5" y="3.5" width="13" height="9"/><path d="M1.5 3.5L8 9l6.5-5.5"/></svg>
        hello@velvetorchidbeauty.com
      </li>
      <li>
        <svg viewBox="0 0 16 16" aria-hidden="true"><circle cx="8" cy="8" r="6.5"/><ellipse cx="8" cy="8" rx="2.8" ry="6.5"/><path d="M1.5 8h13"/></svg>
        velvetorchidbeauty.com
      </li>
    </ul>

    <p class="address">4821 Palm Vista Dr, Sunridge, CA 90000</p>
  </section>
</body>
</html>
```